Women Web Portal

We are developing an internet portal with content created by and for women in Latin America.
This portal will contain different categories focused on relevant topics for women who are at the same time mothers, lovers, workers, pet-owners, ...

We are looking for design that are at the same time uncluttered, easy-to-use and obvious, and comfy. Pastel colours, buttons using traditional fonts, large space for pictures, highlighted social elements,...

Our target being the middle-class women, we want a design that feels comfortable, real, a bit trendy and traditional, not a Tarsk & Welmore design, something women can relate to and feel comfortable enough to come back and participate.

Examples of websites:
www.dishtable.example
mujer.qelvo.example
www.cabellorinva.example
www.fourneau.example
Updates

Hi dear designers. After viewing some first drafts, I have updated the brief so you might have a better understanding of what we are looking for.

Thanks

Reason: We've been away for a while, unavailable to provide adequate feedback to the designs already sent. So we're extending the deadline in order to give time to everyone to adapt their work according to the feedback we'll be providing today.

Target Market(s)

Women between 25 and 50 years from Latin America. Mainly mothers: basically, we want women to interact with each other and with the content of the site so they create a strong community.

Advertisingly speaking, we want to have users, contents and FMCG brands to live together on this website.

Industry/Entity Type

Internet

Requirements
Must have
• Pastel colours for category tabs. Comfortable look & feel.

The design should include 3 different pages:
- Homepage
- Article page
- User profile

The page will be done in responsive design, so design should be thought to be adapted according to the browser (2 or 3 columns).

Thanks for doing it as a PSD file .

The design should also include:
- 8 category tabs
- Space for 728x90px and 300x600px advertising format.
- A relevant menu bar at the beginning of each page
Nice to have
• News feed/best content/most active comments zone: we need to bring forward content to our users so they'll be attracted to visit more pages of the website.

Small format to register (account).

Slider or any other moving objects.

Any idea that would facilitate and increase user participation
Should not have
• Actual text. please use Lorem Ipsum.

```html
<!DOCTYPE html>
<html lang="en">
<head>
<meta charset="utf-8">
<title>vidalinda – Women Portal Homepage</title>
<link href="https://fonts.googleapis.com/css2?family=Roboto+Condensed:wght@400;700&family=Roboto:wght@400;500&display=swap" rel="stylesheet">
<style>
:root{
  --cyan:#1cbce8;
  --cyan-dark:#0aa4d6;
  --cyan-pale:#e4f5fb;
  --pink:#e0607e;
  --orange:#f07a1e;
  --red:#e8283a;
  --ink:#333;
  --grey:#666;
  --panel:#eeeeee;
  --black:#0b0b0b;
}
*{box-sizing:border-box;margin:0;padding:0}
html,body{width:826px;height:1200px;overflow:hidden;background:#fff}
body{position:relative;font-family:"Roboto",Arial,sans-serif;color:var(--ink)}
.abs{position:absolute}
.cond{font-family:"Roboto Condensed","Arial Narrow",sans-serif}
.photo{position:absolute}

/* header */
.top-line{left:0;top:0;width:826px;height:4px;background:var(--cyan)}
.brand{left:86px;top:28px;display:flex;align-items:center;gap:8px}
.brand-name{font-family:"Roboto Condensed",sans-serif;font-size:34px;color:var(--cyan-dark);letter-spacing:.5px}
.brand-dot{width:14px;height:14px;border-radius:50%;background:var(--pink)}
.btn-top{top:19px;height:19px;border-radius:3px;color:#fff;font-size:9px;display:flex;align-items:center;justify-content:center}
.btn-login{left:449px;width:50px;background:var(--cyan)}
.btn-register{left:505px;width:74px;background:var(--pink)}
.search{left:593px;top:17px;width:150px;height:24px;border:1px solid #ddd;border-radius:3px;font-size:7px;color:#777;padding:0 10px;display:flex;align-items:center;justify-content:space-between;box-shadow:0 2px 3px rgba(0,0,0,.06)}

/* nav */
.nav{left:0;top:94px;width:826px;height:48px;background:linear-gradient(#29c7f0,#15b5e4)}
.nav a{position:absolute;top:0;height:48px;line-height:48px;color:#fff;text-decoration:none;font-family:"Roboto Condensed",sans-serif;font-size:12.5px}
.nav .home{left:77px;width:63px;text-align:center;background:var(--pink)}

/* left column */
.news{left:74px;top:146px;width:121px;height:212px;background:var(--panel)}
.news h3{position:absolute;left:8px;top:8px;font-family:"Roboto Condensed",sans-serif;font-weight:400;font-size:12px;color:var(--orange)}
.news-item{position:absolute;left:6px;width:112px;height:46px}
.news-item .thumb{left:0;top:0;width:42px;height:44px;border:2px solid #fff;background:linear-gradient(135deg,#c99a84,#6b4638)}
.news-item p{position:absolute;left:50px;top:0;width:58px;font-size:7.2px;line-height:8.6px;color:#555;text-align:justify}
.news-item p span{color:var(--orange)}

.articles{left:74px;top:358px;width:121px;height:312px;background:var(--black);clip-path:polygon(0 0,100% 0,100% 93%,50% 100%,0 93%);z-index:2}
.articles h3{position:absolute;left:0;width:121px;top:6px;text-align:center;font-family:"Roboto Condensed",sans-serif;font-weight:400;font-size:15px;line-height:17px;color:var(--orange)}
.art-img{left:7px;width:106px;height:71px;border:2px solid #333;background:linear-gradient(135deg,#f3ece6,#c7a58c)}
.play{position:absolute;width:18px;height:18px;border-radius:50%;background:#222}
.play::after{content:"";position:absolute;left:7px;top:5px;border-left:6px solid #fff;border-top:4px solid transparent;border-bottom:4px solid transparent}
.art-cap{left:0;width:121px;text-align:center;font-size:7.3px;line-height:11px;color:#fff}
.art-cap b{display:block;color:var(--orange);font-weight:400;font-size:8.5px}
.btn-cyan{background:var(--cyan);color:#fff;font-family:"Roboto Condensed",sans-serif;font-size:9px;border-radius:3px;display:flex;align-items:center;justify-content:center}
.promo-side{left:74px;top:655px;width:121px;height:305px;clip-path:polygon(0 0,100% 0,100% 95%,50% 100%,0 95%);background:linear-gradient(160deg,#e8c9a8,#b48865 55%,#d7b78f)}
.offer{font-family:"Roboto Condensed",sans-serif;line-height:.95}
.offer .pct{color:#111}
.offer .word{color:var(--red);display:block}

/* banner */
.banner{left:227px;top:147px;width:502px;height:62px;background:linear-gradient(90deg,#e9e9e9 0 34%,#5fa636 34%,#2f7d1c)}
.banner-brand{left:14px;top:20px;font-family:"Roboto Condensed",sans-serif;font-size:15px;color:#333;display:flex;align-items:center;gap:6px}
.banner-brand i{width:16px;height:16px;border-radius:50%;background:#2f7d1c;display:block}
.banner-head{left:172px;top:8px;color:#fff;font-family:"Roboto Condensed",sans-serif;font-size:15px;line-height:16px;text-align:center}
.banner-head small{display:block;font-size:7px;background:#1d5c10;margin-top:2px;padding:1px 3px}
.banner-list{left:322px;top:12px;color:#fff;font-family:"Roboto Condensed",sans-serif;font-size:9.5px;line-height:13px}
.banner-cta{left:426px;top:10px;width:66px;color:#fff;font-size:7px;text-align:center}
.banner-cta span{display:block;margin-top:5px;background:var(--orange);padding:4px 0;font-size:8px;border-radius:2px}

/* hero */
.hero{left:204px;top:218px;width:336px;height:300px;background:linear-gradient(90deg,#f4e9e2 0 40%,#e6c3ae 70%,#d3a590);overflow:hidden}
.hero .offer{position:absolute;left:16px;top:118px;font-size:40px}
.hero .offer .word{margin-left:15px}
.hero-text{left:18px;top:204px;font-family:"Roboto Condensed",sans-serif;font-size:13px;line-height:21px;color:#222}
.hero-btn{left:18px;top:253px;width:131px;height:28px;background:rgba(255,255,255,.75);font-family:"Roboto Condensed",sans-serif;font-size:11.5px;color:#222;display:flex;align-items:center;padding-left:15px}
.hero-btn i{position:absolute;right:7px;top:3px;width:22px;height:22px;border-radius:50%;background:#fff;box-shadow:0 0 2px rgba(0,0,0,.2)}
.hero-btn i::after{content:"";position:absolute;left:9px;top:6px;border-left:6px solid var(--orange);border-top:5px solid transparent;border-bottom:5px solid transparent}
.dot{top:278px;width:8px;height:8px;border-radius:50%;background:#e6d0c6}
.dot.on{background:#5bb8d6}

/* welcome */
.sec-title{font-family:"Roboto Condensed",sans-serif;font-size:16px;color:var(--cyan)}
.welcome-text{left:206px;top:553px;width:332px;font-family:"Roboto Condensed",sans-serif;font-size:8.4px;line-height:13.8px;color:#555;text-align:justify}
.video{left:206px;top:702px;width:330px;height:178px;border:4px solid #f1f1f1;background:linear-gradient(90deg,#f7f3f1 0 30%,#e9cbb8 60%,#d5a991)}
.bigplay{left:140px;top:70px;width:34px;height:34px;border-radius:50%;background:rgba(40,40,40,.75)}
.bigplay::after{content:"";position:absolute;left:13px;top:10px;border-left:10px solid #fff;border-top:7px solid transparent;border-bottom:7px solid transparent}
.progress{left:6px;top:160px;width:284px;height:2px;background:#555}
.vthumb{top:892px;width:102px;height:60px;border:3px solid #f1f1f1}

/* right column */
.ad-side{left:546px;top:220px;width:207px;height:171px;background:linear-gradient(#f6f8fb,#dde6f0);border:1px solid #c7d6e6;text-align:center}
.ad-brand{margin-top:12px;font-size:12px;color:#555}
.ad-brand b{color:#2b6fb5;font-weight:400}
.ad-title{font-size:19px;font-weight:500;color:#1b5fa8;margin-top:4px}
.ad-url{font-size:7px;color:#333}
.ad-url u{color:#1b5fa8}
.ad-list{font-size:7px;line-height:11px;color:#333;margin-top:9px}
.ad-btn{margin:10px auto 0;width:164px;height:24px;border-radius:12px;background:linear-gradient(#f9a24a,#ef7a12);color:#fff;font-size:9.5px;font-weight:500;line-height:24px;box-shadow:0 2px 4px rgba(239,122,18,.4)}
.ad-free{margin-top:10px;font-size:11px;color:#333}

.cat-panel{left:549px;top:398px;width:203px;height:274px;background:#eeeeee}
.panel-tab{position:absolute;top:5px;background:#fff;font-family:"Roboto Condensed",sans-serif;font-size:12px;color:var(--cyan);padding:6px 8px 0;height:26px}
.arrows{position:absolute;top:9px;display:flex;gap:3px}
.arrows i{width:10px;height:10px;border-radius:50%;background:#fff;border:1px solid #ccc;display:block}
.cat-list{position:absolute;left:5px;top:28px;width:193px;height:242px;background:#fff;padding:6px 4px}
.cat-link{height:27px;margin-bottom:2px;background:var(--cyan-pale);font-family:"Roboto Condensed",sans-serif;font-size:10px;color:#333;display:flex;align-items:center;padding-left:12px}
.cat-link::before{content:"";border-left:3px solid var(--cyan);border-top:3px solid transparent;border-bottom:3px solid transparent;margin-right:10px}
.cat-link.active{background:var(--cyan);color:#fff}
.cat-link.active::before{border-left-color:#fff}

.blog-panel{left:549px;top:686px;width:203px;height:280px;background:#eeeeee}
.blog-inner{position:absolute;left:5px;top:5px;width:193px;height:270px;background:#fff}
.blog-tabs{position:absolute;top:11px;font-family:"Roboto Condensed",sans-serif;font-size:12px;color:var(--cyan)}
.post{position:absolute;left:10px;width:180px;height:72px}
.post .pimg{left:0;top:0;width:61px;height:53px;border:2px solid #ddd}
.post h4{position:absolute;left:70px;top:0;width:108px;font-family:"Roboto Condensed",sans-serif;font-weight:400;font-size:8.6px;line-height:11px;color:#333;text-align:justify}
.post p{position:absolute;left:70px;top:24px;width:106px;font-family:"Roboto Condensed",sans-serif;font-size:7.8px;line-height:10px;color:#888}
.post .date{position:absolute;left:70px;top:61px;font-family:"Roboto Condensed",sans-serif;font-size:8px;color:#333}
.post .count{position:absolute;left:149px;top:58px;width:19px;height:14px;background:#f3a31a;color:#333;font-size:7.5px;display:flex;align-items:center;justify-content:center}

.divider{left:74px;top:986px;width:680px;height:1px;background:#e4e4e4}

/* footer */
.footer{left:0;top:996px;width:826px;height:204px;background:linear-gradient(#22c1ec,#12a9dc)}
.footer h5{position:absolute;font-family:"Roboto Condensed",sans-serif;font-weight:400;font-size:12px;color:#fff}
.quick{position:absolute;top:44px;list-style:none;font-family:"Roboto Condensed",sans-serif;font-size:8.4px;color:#fff;line-height:19.2px}
.quick li::before{content:"•";margin-right:4px}
.nl-input{left:316px;top:43px;width:191px;height:24px;background:#fff;border-radius:12px;font-family:"Roboto Condensed",sans-serif;font-size:8.6px;color:#777;display:flex;align-items:center;padding-left:30px}
.nl-input i{position:absolute;left:10px;top:7px;width:14px;height:10px;border:1px solid #999}
.nl-note{left:400px;top:76px;font-family:"Roboto Condensed",sans-serif;font-size:9px;color:#fff}
.nl-btn{left:414px;top:98px;width:102px;height:24px;background:linear-gradient(#fbb13a,#ef7d12);color:#fff;font-family:"Roboto Condensed",sans-serif;font-weight:700;font-size:11px;display:flex;align-items:center;justify-content:center;border-radius:2px;box-shadow:0 3px 5px rgba(0,0,0,.15)}
.tweet{left:562px;top:48px;width:158px;height:80px;background:rgba(255,255,255,.18);border-radius:4px;font-family:"Roboto Condensed",sans-serif;font-size:7.8px;line-height:12.5px;color:#fff;padding:9px 12px}
.social{top:160px;width:20px;height:20px;border-radius:50%;background:#fff}
.copy{left:93px;top:169px;font-size:7.5px;color:#fff}
</style>
</head>
<body>

<div class="abs top-line"></div>

<header>
  <div class="abs brand"><span class="brand-name">vidalinda</span><span class="brand-dot"></span></div>
  <div class="abs btn-top btn-login">LOGIN</div>
  <div class="abs btn-top btn-register">REGISTER</div>
  <div class="abs search"><span>Search</span>
    <svg width="11" height="11" viewBox="0 0 11 11"><circle cx="4.5" cy="4.5" r="3.5" fill="none" stroke="#888" stroke-width="1.3"/><line x1="7" y1="7" x2="10" y2="10" stroke="#888" stroke-width="1.5"/></svg>
  </div>
</header>

<nav class="abs nav">
  <a class="home">Home</a>
  <a style="left:146px">About us</a>
  <a style="left:214px">Services</a>
  <a style="left:277px">Latest Articles</a>
  <a style="left:369px">News and Events</a>
  <a style="left:476px">Categorys</a>
  <a style="left:549px">Find your Idel Partner</a>
  <a style="left:678px">Contact us</a>
</nav>

<!-- left column -->
<aside class="abs news">
  <h3>Latest News / Events</h3>
  <div class="news-item" style="top:32px"><div class="photo thumb" role="img" aria-label="Portrait of a smiling woman"></div><p><span>Lorem Ipsum is simply</span> dummy text of the printing and typesetting</p></div>
  <div class="news-item" style="top:93px"><div class="photo thumb" role="img" aria-label="Portrait of a smiling woman"></div><p><span>Lorem Ipsum is simply</span> dummy text of the printing and typesetting</p></div>
  <div class="news-item" style="top:155px"><div class="photo thumb" role="img" aria-label="Portrait of a smiling woman"></div><p><span>Lorem Ipsum is simply</span> dummy text of the printing and typesetting</p></div>
</aside>

<section class="abs articles">
  <h3>LATEST<br>ARTICLES</h3>
  <div class="photo art-img" style="top:43px" role="img" aria-label="Woman relaxing during a spa treatment"><span class="play" style="left:42px;top:26px"></span></div>
  <div class="abs art-cap" style="top:118px"><b>Contrary to popular belief</b>Lorem Ipsum is not simply<br>random text</div>
  <div class="photo art-img" style="top:164px" role="img" aria-label="Woman relaxing during a spa treatment"></div>
  <div class="abs art-cap" style="top:244px"><b>Contrary to popular belief</b>Lorem Ipsum is not simply<br>random text</div>
  <div class="abs btn-cyan" style="left:27px;top:288px;width:66px;height:19px">Read More</div>
</section>

<div class="photo promo-side" role="img" aria-label="Woman resting with a flower in her hair at a spa">
  <div class="abs offer" style="left:22px;top:177px;font-size:38px"><span class="pct">50%</span><span class="word">Offer</span></div>
</div>

<!-- banner ad -->
<div class="abs banner">
  <div class="abs banner-brand"><i></i>Norvia Hosting</div>
  <div class="abs banner-head">UP TO 300%<br>FASTER HOSTING<small>NOW FEATURING SSD HOSTING!</small></div>
  <div class="abs banner-list">➔ RapidCore Platform<br>➔ Expert Team Support<br>➔ Ultra-Reliable</div>
  <div class="abs banner-cta">PRIME HOSTING +SSD<span>Learn More</span></div>
</div>

<!-- hero slider -->
<section class="photo hero" role="img" aria-label="Close-up of a woman with clear skin touching her face">
  <div class="offer" style="position:absolute;left:16px;top:118px;font-size:40px"><span class="pct">50%</span><span class="word" style="margin-left:15px">Offer</span></div>
  <div class="abs hero-text">SED UT PERSPICIATIS UNDE OMNIS ISTE NATUS ERROR<br>SIT VOLUPTATEM ACCUSANTIUM</div>
  <div class="abs hero-btn">REGISTER NOW<i></i></div>
  <span class="abs dot" style="left:282px"></span>
  <span class="abs dot" style="left:297px"></span>
  <span class="abs dot on" style="left:311px"></span>
</section>

<!-- welcome -->
<h2 class="abs sec-title" style="left:205px;top:529px;font-weight:400">WELCOME</h2>
<p class="abs welcome-text">Sed ut perspiciatis unde omnis iste natus error sit voluptatem accusantium doloremque laudantium, totam rem aperiam, eaque ipsa quae ab illo inventore veritatis et quasi architecto beatae vitae dicta sunt explicabo. Nemo enim ipsam voluptatem quia voluptas sit aspernatur aut odit aut fugit, sed quia consequuntur magni dolores eos qui ratione voluptatem sequi nesciunt. Neque porro quisquam est, qui dolorem ipsum quia dolor sit amet, consectetur, adipisci</p>
<div class="abs btn-cyan" style="left:470px;top:641px;width:66px;height:19px">Read More</div>

<h2 class="abs sec-title" style="left:206px;top:672px;font-weight:400">FEATURED VIDEO</h2>
<div class="photo video" role="img" aria-label="Woman with a white lily, beauty video still">
  <span class="abs bigplay"></span>
  <span class="abs progress"></span>
</div>
<div class="photo vthumb" style="left:206px;background:linear-gradient(90deg,#f6f1ee,#d9a88f)" role="img" aria-label="Woman holding a flower"><span class="play" style="left:42px;top:18px;opacity:.7"></span></div>
<div class="photo vthumb" style="left:321px;background:linear-gradient(90deg,#e9e2c8,#c7b08a)" role="img" aria-label="Woman receiving a massage"><span class="play" style="left:42px;top:18px;opacity:.7"></span></div>
<div class="photo vthumb" style="left:435px;background:linear-gradient(90deg,#f4efee,#cfa38c)" role="img" aria-label="Woman relaxing near flowers"><span class="play" style="left:42px;top:18px;opacity:.7"></span></div>

<!-- right column -->
<aside class="abs ad-side">
  <div class="ad-brand">Wordwell <b>@edu</b></div>
  <div class="ad-title">Get Writing Support</div>
  <div class="ad-url">at <u>www.wordwell.example/edu</u></div>
  <div class="ad-list">Automated Grammar Tutor<br>Revision Tool<br>Citation Checker</div>
  <div class="ad-btn">Use your school email to sign up</div>
  <div class="ad-free">It's FREE!</div>
</aside>

<section class="abs cat-panel">
  <div class="cat-list">
    <div class="cat-link active">Category Link 1</div>
    <div class="cat-link">Category Link 2</div>
    <div class="cat-link">Category Link 3</div>
    <div class="cat-link">Category Link 4</div>
    <div class="cat-link">Category Link 5</div>
    <div class="cat-link">Category Link 6</div>
    <div class="cat-link">Category Link 7</div>
    <div class="cat-link">Category Link 8</div>
  </div>
  <div class="panel-tab" style="left:5px">CATEGORIES</div>
  <div class="arrows" style="left:165px"><i></i><i></i></div>
</section>

<section class="abs blog-panel">
  <div class="blog-inner">
    <span class="blog-tabs" style="left:15px">BLOG</span>
    <span class="blog-tabs" style="left:57px">POPULAR</span>
    <span class="blog-tabs" style="left:128px">COMMENTS</span>
    <article class="post" style="top:36px">
      <div class="photo pimg" style="background:linear-gradient(#4f86c6,#1e3f6e)" role="img" aria-label="Climber on a rock at dusk"></div>
      <h4>CONTRARY TO POPULAR BELIEF, LOREM IPSUM</h4>
      <p>There are many variations of passages of Lorem Ipsum available,</p>
      <span class="date">February 1, 2013</span><span class="count">10</span>
    </article>
    <article class="post" style="top:114px">
      <div class="photo pimg" style="background:linear-gradient(#8fb0cc,#b65a3a)" role="img" aria-label="Runners on a track"></div>
      <h4>CONTRARY TO POPULAR BELIEF, LOREM IPSUM</h4>
      <p>There are many variations of passages of Lorem Ipsum available,</p>
      <span class="date">February 1, 2013</span><span class="count">10</span>
    </article>
    <article class="post" style="top:191px">
      <div class="photo pimg" style="background:linear-gradient(135deg,#f7e6ea,#d94f6e)" role="img" aria-label="Close-up of red lips and nails"></div>
      <h4>CONTRARY TO POPULAR BELIEF, LOREM IPSUM</h4>
      <p>There are many variations of passages of Lorem Ipsum available,</p>
      <span class="date">February 1, 2013</span><span class="count">10</span>
    </article>
  </div>
</section>

<div class="abs divider"></div>

<!-- footer -->
<footer class="abs footer">
  <h5 style="left:90px;top:16px">Quick Links</h5>
  <ul class="quick" style="left:90px"><li>Integer lobortis</li><li>Curabitur ac</li><li>Phasellus tellus nisl</li><li>Aenean fringilla</li><li>Vestibulum</li><li>Aliquam commodo</li></ul>
  <ul class="quick" style="left:208px"><li>Integer lobortis</li><li>Curabitur ac</li><li>Phasellus tellus nisl</li><li>Aenean fringilla</li><li>Vestibulum</li><li>Aliquam commodo</li></ul>

  <h5 style="left:311px;top:16px">Newsletter</h5>
  <div class="abs nl-input"><i></i>Subscribe your news letter</div>
  <div class="abs nl-note">Subscribe your news letter</div>
  <div class="abs nl-btn">SUBSCRIBE</div>

  <h5 style="left:562px;top:26px">Chirper Updates</h5>
  <div class="abs tweet">@lumathemes there is a new designer in town people!<br><br>Check it out: http://lnk.example</div>

  <span class="abs social" style="left:582px"></span>
  <span class="abs social" style="left:611px"></span>
  <span class="abs social" style="left:640px"></span>
  <span class="abs social" style="left:668px"></span>
  <span class="abs social" style="left:697px">
    <svg width="20" height="20" viewBox="0 0 20 20"><path d="M10 5v10M5 10h10" stroke="#12a9dc" stroke-width="2.4"/></svg>
  </span>

  <div class="abs copy">Copyright © 2013 &nbsp;www.vidalinda.example &nbsp;All rights reserved.</div>
</footer>

</body>
</html>
```